Autobody repair paint repairs spray painting bodywork crash repairs

Details for my new Facebook Design Project will be added sooAUTOMOTIVE REPAIR. CAR / MOTORCYCLES GOT LOGO DESIGN / DID THINK ABOUT FACEBOOK DONT NOALREADY HAVE WEB ADRESS www.brenvaro.co.uk and mail sales@brenvaro,co.uk NEED SOMETHINK I CAN MANAGE TO UPLOAD PICTURES IN TO A GALLERY OR SOMETHINGLIKE THAT I ALSO SELL CAR AND MOTORCYCLES MAYBE A SELLS PAGE WITH A QUIDLOOP LINKn.

Target Market(s)

general public and trade

Industry/Entity Type

Auto Repair

Font styles to use
Serif
Sans Serif

Colors

Designer to choose colors to be used in the design.

Requirements
Must have
• copy description from my website
• quidloop link. to my site shop
• plenty of logo within reason
Nice to have
• scolling shop
• easy to manage

```html
<!DOCTYPE html>
<html lang="en">
<head>
<meta charset="utf-8">
<title>Brenvaro Bodyshop – Automotive Repair</title>
<link href="https://fonts.googleapis.com/css2?family=Passion+One:wght@400;700&family=Open+Sans:wght@700;800&family=Raleway:wght@700&family=Exo+2:wght@800&display=swap" rel="stylesheet">
<style>
  :root {
    --black: #000000;
    --asphalt: #2b2a2a;
    --red: #e52a2f;
    --red-dark: #a8161c;
    --maroon: #8e0d10;
    --white: #ffffff;
    --car-red: #c8161c;
  }
  * { margin: 0; padding: 0; box-sizing: border-box; }
  html, body { width: 1200px; height: 675px; overflow: hidden; background: var(--black); }
  .page { position: relative; width: 1200px; height: 675px; overflow: hidden; }

  .site-nav {
    height: 42px; background: var(--black);
    display: flex; justify-content: center; align-items: center; gap: 52px;
    font-family: "Raleway", sans-serif; font-weight: 700; font-size: 12px;
    color: var(--white); letter-spacing: 0.2px;
  }

  .hero { position: absolute; top: 42px; left: 0; width: 1200px; height: 633px; overflow: hidden; }
  .hero-backdrop {
    position: absolute; inset: 0;
    background: linear-gradient(180deg, #121214 0%, #2a2522 45%, #3a2f24 52%, var(--asphalt) 62%, #161616 100%);
  }
  .hero-swoosh { position: absolute; inset: 0; }

  .headline {
    position: absolute; left: 93px; top: 128px; width: 400px; text-align: center;
    font-family: "Passion One", sans-serif; font-weight: 700; text-transform: uppercase;
    color: var(--maroon);
    -webkit-text-stroke: 7px var(--white); paint-order: stroke fill;
    line-height: 0.98;
  }
  .headline .line-1 { display: block; font-size: 72px; letter-spacing: 0.5px; }
  .headline .line-2 { display: block; font-size: 92px; letter-spacing: 2px; }

  .services {
    position: absolute; left: 30px; top: 322px; width: 522px; text-align: center;
    font-family: "Open Sans", sans-serif; font-weight: 800; font-size: 12.5px;
    color: var(--white); letter-spacing: 1.9px; line-height: 22px; white-space: nowrap;
  }

  .shop-button {
    position: absolute; left: 206px; top: 402px; width: 170px; height: 42px;
    border-radius: 5px;
    background: linear-gradient(180deg, #f0393c 0%, var(--red) 50%, var(--red-dark) 100%);
    box-shadow: 0 3px 6px rgba(0,0,0,0.5);
    display: flex; align-items: center; justify-content: center;
    font-family: "Open Sans", sans-serif; font-weight: 800; font-size: 20px;
    color: var(--white); letter-spacing: 1.5px;
  }

  .pay-row {
    position: absolute; left: 95px; top: 484px;
    display: flex; align-items: center; gap: 10px;
    font-family: "Open Sans", sans-serif; font-weight: 700; color: var(--white);
  }
  .pay-mark { width: 24px; height: 24px; border-radius: 50%; background: var(--white); }
  .pay-label { font-size: 15.5px; }
  .pay-link {
    margin-left: 4px; background: var(--white); color: #111; border-radius: 5px;
    padding: 3px 8px; font-size: 14px;
  }

  .brand {
    position: absolute; left: 866px; top: 48px; width: 270px; text-align: center;
    font-family: "Exo 2", sans-serif; font-weight: 800; color: var(--white);
  }
  .brand-name { display: block; font-size: 40px; letter-spacing: 2px; line-height: 1; }
  .brand-tag { display: block; margin-top: 8px; font-size: 12px; letter-spacing: 8px; }

  .car-photo {
    position: absolute; left: 540px; top: 222px; width: 630px; height: 300px;
    background: linear-gradient(160deg, #3a1012 0%, var(--car-red) 35%, #b3161b 60%, #4a0c0e 100%);
  }
</style>
</head>
<body>
<div class="page">
  <nav class="site-nav">
    <span>HOME</span><span>ABOUT US</span><span>SERVICE</span><span>CUSTOM</span><span>GALLERY</span><span>CONTACT</span>
  </nav>

  <section class="hero">
    <div class="hero-backdrop" role="img" aria-label="Night sky over a desert road with a warning sign"></div>
    <svg class="hero-swoosh" width="1200" height="633" viewBox="0 0 1200 633" aria-hidden="true">
      <defs>
        <linearGradient id="swooshRed" x1="0" y1="0" x2="1" y2="0">
          <stop offset="0" stop-color="#f0373b"/>
          <stop offset="1" stop-color="#c91d22"/>
        </linearGradient>
      </defs>
      <path d="M0,18 C260,-8 540,110 700,244 C520,150 300,140 0,300 Z" fill="url(#swooshRed)"/>
      <path d="M0,300 C300,140 520,150 700,244 C500,175 290,185 0,318 Z" fill="#8a1014"/>
    </svg>

    <h1 class="headline"><span class="line-1">Automotive</span><span class="line-2">Repair</span></h1>
    <p class="services">AUTOMOTIVE BODY REPAIRS | MOTORCYCLE PAINTING<br>WHEELS | BUMPERS | CUSTOM PAINTING</p>
    <div class="shop-button">SHOP NOW</div>

    <div class="pay-row">
      <span class="pay-mark"></span>
      <span class="pay-label">Pay with Quidloop</span>
      <span class="pay-link">quidloop.me/rokhandel0012</span>
    </div>

    <div class="brand">
      <span class="brand-name">BRENVARO</span>
      <span class="brand-tag">BODYSHOP</span>
    </div>

    <div class="car-photo" role="img" aria-label="Photo of a glossy red sports coupe with headlights on"></div>
  </section>
</div>
</body>
</html>
```